Business card design needed

Double sided
Color, unique, elegant

Maybe put this quote somewhere?? But I think it might make it to cluttered?
“The Pilates Method of Body
Conditioning develops the body
uniformly, corrects posture, restores
vitality, invigorates the mind and
elevates the spirit”
- Henrik Dovacombe

Industry/Entity Type

Business

Contact Information for Business Card

Marta Kellbrook
Pilates Instructor & Personal trainer
Mobile: 0498265043
www.lorvix.com.au
email: lorvixhealth.fitness@qentamail.com

```html
<!DOCTYPE html>
<html lang="en">
<head>
<meta charset="utf-8">
<title>Lorvix Health and Fitness – Business Card</title>
<link rel="stylesheet" href="https://fonts.googleapis.com/css2?family=Jost:wght@300;400;500&family=Libre+Baskerville&display=swap">
<style>
  :root {
    --magenta: #a6236f;
    --magenta-deep: #7e1f58;
    --magenta-soft: #c0588f;
    --plum-ink: #2a1024;
    --leaf-green: #7dbb5a;
    --paper: #ffffff;
    --backdrop: #eeeeee;
    --blush: #f3d9e7;
  }
  * { box-sizing: border-box; margin: 0; padding: 0; }
  html, body { width: 1200px; height: 900px; overflow: hidden; }
  body {
    background: var(--backdrop);
    font-family: "Jost", "Futura", sans-serif;
    display: flex;
    align-items: center;
    justify-content: center;
    gap: 40px;
  }
  .card {
    width: 550px;
    height: 322px;
    position: relative;
    overflow: hidden;
    box-shadow: 0 2px 10px rgba(0,0,0,0.12);
  }

  /* Information side */
  .card--info { background: var(--paper); }
  .photo-band {
    position: absolute;
    left: 0; top: 0;
    width: 100%; height: 208px;
    background: linear-gradient(180deg, var(--magenta-soft) 0%, var(--magenta) 55%, var(--magenta-deep) 100%);
  }
  .band-brand {
    position: absolute;
    left: 34px; top: 40px;
    color: var(--blush);
    text-align: center;
  }
  .band-brand__name {
    font-weight: 300;
    font-size: 30px;
    letter-spacing: 4px;
    line-height: 1;
  }
  .band-brand__tagline {
    font-weight: 400;
    font-size: 12px;
    margin-top: 4px;
  }
  .quote {
    position: absolute;
    right: 18px; top: 20px;
    width: 300px;
    color: var(--paper);
    text-align: center;
    font-family: "Libre Baskerville", "Times New Roman", serif;
    font-size: 11.5px;
    line-height: 1.45;
  }
  .quote__source {
    display: block;
    font-family: "Jost", sans-serif;
    font-size: 8px;
    margin-top: 2px;
  }
  .holder {
    position: absolute;
    left: 22px; top: 238px;
  }
  .holder__name {
    color: var(--plum-ink);
    font-weight: 400;
    font-size: 24px;
    letter-spacing: 1px;
    font-variant: small-caps;
    line-height: 1;
  }
  .holder__role {
    color: var(--leaf-green);
    font-size: 14px;
    margin-top: 6px;
  }
  .contact {
    position: absolute;
    right: 24px; top: 230px;
    text-align: right;
    color: var(--plum-ink);
    font-size: 14px;
    line-height: 1.35;
    list-style: none;
  }

  /* Brand side */
  .card--brand {
    background: var(--magenta);
    display: flex;
    flex-direction: column;
    align-items: center;
    justify-content: center;
    color: var(--paper);
  }
  .brand-dot {
    width: 26px; height: 26px;
    border-radius: 50%;
    background: var(--leaf-green);
    margin-bottom: 18px;
  }
  .brand-name {
    font-weight: 300;
    font-size: 40px;
    letter-spacing: 6px;
    line-height: 1;
  }
  .brand-tagline {
    font-size: 14px;
    margin-top: 6px;
  }
</style>
</head>
<body>
  <section class="card card--info">
    <div class="photo-band" role="img" aria-label="Photo of a woman in a Pilates swan pose holding a Pilates ring, tinted magenta"></div>
    <div class="band-brand">
      <div class="band-brand__name">LORVIX</div>
      <div class="band-brand__tagline">Health and Fitness</div>
    </div>
    <blockquote class="quote">
      “The Pilates Method of Body Conditioning develops the body uniformly, corrects posture, restores vitality, invigorates the mind and elevates the spirit”
      <span class="quote__source">- Henrik Dovacombe</span>
    </blockquote>
    <div class="holder">
      <div class="holder__name">Marta Kellbrook</div>
      <div class="holder__role">Pilates Instructor &amp; Personal trainer</div>
    </div>
    <ul class="contact">
      <li>Mobile. 0498265043</li>
      <li>www.lorvix.com.au</li>
      <li>lorvixhealth.fitness@qentamail.com</li>
    </ul>
  </section>

  <section class="card card--brand">
    <div class="brand-dot"></div>
    <div class="brand-name">LORVIX</div>
    <div class="brand-tagline">Health and Fitness</div>
  </section>
</body>
</html>
```